Carla Vennet Independent Sales rep business card

I am and independent sales rep I currently rep 3 furniture lines and 1 art line
I need the logos of each line I represent on my business card
I would prefer to have one sided card but if it works better to have all logos on the back side then I will consider
If you need high res versions of logos please let me know asap
THX

Business

Carla Mosley Vennet
Independent Sales Rep
carla@vennetmail.com
555.418.6072

```html
<!DOCTYPE html>
<html lang="en">
<head>
<meta charset="utf-8">
<title>Carla Mosley Vennet – Business Card</title>
<link href="https://fonts.googleapis.com/css2?family=Questrial&family=Montserrat:wght@600&family=Source+Sans+3:wght@400;600&display=swap" rel="stylesheet">
<style>
  :root {
    --backdrop: #a8a5a6;
    --card-dark: #151618;
    --card-light: #fbfbfb;
    --ink: #1d1d1f;
    --ink-soft: #3a3a3c;
    --gold: #f2c018;
    --divider: #e3e3e3;
    --white: #ffffff;
  }
  * { box-sizing: border-box; margin: 0; padding: 0; }
  html, body { width: 1200px; height: 1200px; overflow: hidden; }
  body { background: var(--backdrop); position: relative; font-family: "Source Sans 3", sans-serif; }

  .card { position: absolute; width: 712px; border-radius: 28px; overflow: hidden; }

  /* Front face */
  .card-front { left: 238px; top: 118px; height: 419px; background: var(--card-dark); color: var(--white); text-align: center; }
  .front-name { position: absolute; top: 150px; left: 0; right: 0; font-family: "Questrial", sans-serif; font-size: 62px; line-height: 1; letter-spacing: 0.5px; }
  .front-company { position: absolute; top: 226px; left: 0; right: 0; font-family: "Questrial", sans-serif; font-size: 35px; line-height: 1; }
  .front-rule { position: absolute; top: 244px; width: 84px; height: 3px; }
  .front-rule.left { left: 194px; }
  .front-rule.right { left: 435px; }

  /* Back face */
  .card-back { left: 231px; top: 645px; height: 415px; background: var(--card-light); color: var(--ink); }
  .lines { position: absolute; left: 60px; width: 246px; top: 70px; text-align: center; color: var(--ink-soft); }
  .line-name { display: block; font-family: "Source Sans 3", sans-serif; font-weight: 400; }
  .line-marlo { font-size: 15px; letter-spacing: 3.5px; text-transform: uppercase; margin-top: 38px; }
  .line-owen { font-size: 17px; line-height: 16px; margin-top: 24px; }
  .line-lena { font-size: 17px; margin-top: 22px; }
  .line-tessa { font-size: 30px; line-height: 1; margin-top: 10px; }

  .divider { position: absolute; left: 368px; top: 43px; width: 1px; height: 272px; background: var(--divider); }

  .contact { position: absolute; left: 417px; top: 140px; }
  .contact-name { font-family: "Montserrat", sans-serif; font-weight: 600; font-size: 22px; letter-spacing: 0.3px; margin-bottom: 20px; }
  .contact-row { display: flex; align-items: center; gap: 12px; font-size: 20px; line-height: 32px; }
  .contact-row svg { width: 16px; height: 14px; flex: none; }

  .band { position: absolute; left: 0; bottom: 0; width: 712px; height: 53px; }
  .role { position: absolute; left: 416px; top: 376px; font-size: 17px; color: var(--white); letter-spacing: 0.2px; }
</style>
</head>
<body>

<section class="card card-front">
  <h1 class="front-name">Carla Mosley</h1>
  <svg class="front-rule left" viewBox="0 0 84 3"><defs><linearGradient id="ruleL"><stop offset="0" stop-color="#f2c018" stop-opacity="0"/><stop offset="1" stop-color="#f2c018"/></linearGradient></defs><rect width="84" height="2" y="0.5" fill="url(#ruleL)"/></svg>
  <p class="front-company">Vennet</p>
  <svg class="front-rule right" viewBox="0 0 84 3"><defs><linearGradient id="ruleR"><stop offset="0" stop-color="#f2c018"/><stop offset="1" stop-color="#f2c018" stop-opacity="0"/></linearGradient></defs><rect width="84" height="2" y="0.5" fill="url(#ruleR)"/></svg>
</section>

<section class="card card-back">
  <div class="lines">
    <span class="line-name line-marlo">Marlo Deventi</span>
    <span class="line-name line-owen">Owen Hartfield<br>Gallery</span>
    <span class="line-name line-lena">Lena Ocampo</span>
    <span class="line-name line-tessa">Tessa Lorne Home</span>
  </div>

  <div class="divider"></div>

  <div class="contact">
    <p class="contact-name">Carla Mosley Vennet</p>
    <p class="contact-row">
      <svg viewBox="0 0 16 14"><path d="M1 5c0-2 3-3.5 7-3.5S15 3 15 5v1.2h-3.5V4.6H4.5v1.6H1Z M3.5 7h9l2 6h-13Z" fill="#1d1d1f"/><circle cx="8" cy="9.8" r="1.6" fill="#fbfbfb"/></svg>
      555.418.6072
    </p>
    <p class="contact-row">
      <svg viewBox="0 0 16 14"><rect x="1" y="2.5" width="14" height="10" fill="#1d1d1f"/><path d="M1.5 3l6.5 5 6.5-5" stroke="#fbfbfb" stroke-width="1.2" fill="none"/></svg>
      carla@vennetmail.com
    </p>
  </div>

  <svg class="band" viewBox="0 0 712 53" preserveAspectRatio="none">
    <rect x="0" y="27" width="362" height="26" fill="#f2c018"/>
    <polygon points="341,53 377,0 712,0 712,53" fill="#151618"/>
  </svg>
  <p class="role">Independent Sales Rep</p>
</section>

</body>
</html>
```